Business card Zottelgarten

Business card is for a self-employed dog trainer with own dog school. Name and logo of the dog school are available. Color specifications as well. The design should be classy and minimalist, but also modern. An already existing idea would be: Front: Only the logo Back: Contact data

Font styles to use
Serif
Sans Serif
Other font styles liked:
• Trajan Pro

Colors
f78f20

Requirements
Must have
• Name: Margit Wendler-Rasch Title: Dipl. Dog Trainer Contain my logo Follow my font and color preferences (see files)

```html
<!DOCTYPE html>
<html lang="de">
<head>
<meta charset="utf-8">
<title>Zottelgarten – Business Card</title>
<link href="https://fonts.googleapis.com/css2?family=Cinzel:wght@400;500&family=Lato:wght@400&display=swap" rel="stylesheet">
<style>
  :root {
    --stage: #2e2e2f;
    --card: #7e6c5e;
    --card-faint: #8b796b;
    --card-faint-line: #95837566;
    --ink: #f4efe9;
    --ink-soft: #e6ddd3;
    --accent: #f78f20;
  }
  html, body {
    margin: 0;
    width: 1200px;
    height: 900px;
    overflow: hidden;
    background: var(--stage);
  }
  .stage {
    position: relative;
    width: 1200px;
    height: 900px;
  }
  .card {
    position: absolute;
    width: 660px;
    height: 377px;
    background: var(--card);
    overflow: hidden;
    box-shadow: 0 14px 30px rgba(0,0,0,.45);
  }
  .card--front { left: 90px; top: 62px; }
  .card--back { left: 450px; top: 468px; }

  .faint-ring {
    position: absolute;
    border-radius: 50%;
    background: var(--card-faint);
    border: 3px solid var(--card-faint-line);
    box-sizing: border-box;
  }
  .card--front .faint-ring { width: 330px; height: 330px; left: -70px; top: 120px; }
  .card--back .faint-ring { width: 300px; height: 300px; right: -80px; top: -40px; }

  .brand {
    position: absolute;
    text-align: center;
    color: var(--ink);
  }
  .card--front .brand { left: 0; right: 0; top: 50px; }
  .brand-mark {
    width: 150px;
    height: 150px;
    border-radius: 50%;
    background: var(--ink);
    margin: 0 auto 22px;
  }
  .brand-name {
    font-family: "Cinzel", serif;
    font-weight: 400;
    font-size: 38px;
    letter-spacing: 3px;
    line-height: 1;
    margin: 0;
  }
  .brand-url {
    font-family: "Cinzel", serif;
    font-size: 9.5px;
    letter-spacing: 5.2px;
    margin-top: 4px;
  }

  .card--back .brand { left: 95px; top: 70px; text-align: left; }
  .card--back .brand-name { font-size: 24px; letter-spacing: 2px; }
  .card--back .brand-url { font-size: 6.5px; letter-spacing: 3.3px; margin-top: 3px; }

  .edge-rule {
    position: absolute;
    left: 55px;
    top: 145px;
    width: 5px;
    height: 150px;
    background: var(--ink);
  }
  .edge-tab {
    position: absolute;
    left: 55px;
    top: 172px;
    width: 20px;
    height: 24px;
    background: var(--accent);
  }

  .person {
    position: absolute;
    left: 95px;
    top: 160px;
    color: var(--ink);
  }
  .person-name {
    font-family: "Cinzel", serif;
    font-size: 17px;
    letter-spacing: 1px;
    margin: 0;
  }
  .person-title {
    font-family: "Lato", sans-serif;
    font-size: 14px;
    color: var(--ink-soft);
    margin-top: 2px;
  }

  .contacts {
    position: absolute;
    left: 122px;
    top: 232px;
    margin: 0;
    padding: 0;
    list-style: none;
    font-family: "Lato", sans-serif;
    font-size: 14.5px;
    letter-spacing: .6px;
    color: var(--ink-soft);
  }
  .contacts li {
    display: flex;
    align-items: center;
    gap: 12px;
    height: 24px;
  }
  .contacts svg { width: 14px; height: 14px; flex: none; }
</style>
</head>
<body>
<div class="stage">

  <section class="card card--front" aria-label="Card front">
    <div class="faint-ring" role="img" aria-label="Faint background circle with dog silhouette"></div>
    <div class="brand">
      <div class="brand-mark"></div>
      <p class="brand-name">ZOTTELGARTEN</p>
      <div class="brand-url">WWW.ZOTTELGARTEN.CH</div>
    </div>
  </section>

  <section class="card card--back" aria-label="Card back">
    <div class="faint-ring" role="img" aria-label="Faint background circle with dog silhouette"></div>
    <div class="brand">
      <p class="brand-name">ZOTTELGARTEN</p>
      <div class="brand-url">WWW.ZOTTELGARTEN.CH</div>
    </div>

    <div class="edge-rule"></div>
    <div class="edge-tab"></div>

    <div class="person">
      <p class="person-name">MARGIT WENDLER-RASCH</p>
      <div class="person-title">Dipl. Dog Trainer</div>
    </div>

    <ul class="contacts">
      <li>
        <svg viewBox="0 0 14 14" fill="none" stroke="#f4efe9" stroke-width="1.2"><circle cx="7" cy="7" r="6.2"/><path d="M4.6 4c.3-.3.8-.3 1 0l.7 1c.2.3.1.6-.1.8l-.4.3c.4.8 1 1.4 1.8 1.8l.3-.4c.2-.2.5-.3.8-.1l1 .7c.3.2.3.7 0 1-.5.6-1.3.7-2 .4C6.3 9 5 7.7 4.3 6.3c-.3-.8-.2-1.6.3-2.3z"/></svg>
        <span>(123) 456-7890</span>
      </li>
      <li>
        <svg viewBox="0 0 14 14" fill="none" stroke="#f4efe9" stroke-width="1.2"><circle cx="7" cy="7" r="6.2"/><rect x="3.8" y="4.8" width="6.4" height="4.4"/><path d="M3.8 4.8 7 7.4l3.2-2.6"/></svg>
        <span>margit@zottelgarten.com</span>
      </li>
      <li>
        <svg viewBox="0 0 14 14" fill="none" stroke="#f4efe9" stroke-width="1.2"><circle cx="7" cy="7" r="6.2"/><ellipse cx="7" cy="7" rx="2.4" ry="6.2"/><path d="M1 7h12M2 4.2h10M2 9.8h10"/></svg>
        <span>www.zottelgarten.ch</span>
      </li>
    </ul>
  </section>

</div>
</body>
</html>
```